Letterhead for a busy but slightly unconventional doctor

I need a letterhead for a busy and senior London based medical doctor who specialises in psychiatry.
Letterhead needs to say
Dr Lena Morwen Ostrow MA PhD MRCP MRCPsych
BPR number 3819057
17, Calloway Street
London N4K 2TB
Telephone: 07812 430276
Email: lena.m.ostrow@dovrel.ac.uk
Letterhead needs to be greyscale or black and white. I would like a classic but contemporary look but a bit quirky/unusual.
I will print on pale grey paper so needs to look good with that.
Something a little bit unconventional.
other doctors and patients
Doctor

```html
<!DOCTYPE html>
<html lang="en">
<head>
<meta charset="utf-8">
<title>Letterhead – Dr Lena Morwen Ostrow</title>
<link rel="stylesheet" href="https://fonts.googleapis.com/css2?family=Fira+Sans:wght@400;600;700&family=Crimson+Pro:wght@400&display=swap">
<style>
  :root {
    --paper: #ffffff;
    --ink: #1c1c1c;
    --ink-soft: #3a3a3a;
    --rule: #555555;
  }
  * { margin: 0; padding: 0; box-sizing: border-box; }
  html, body {
    width: 849px;
    height: 1200px;
    overflow: hidden;
    background: var(--paper);
  }
  .sheet {
    position: relative;
    width: 849px;
    height: 1200px;
    background: var(--paper);
    color: var(--ink);
  }
  .identity {
    position: absolute;
    left: 283px;
    top: 128px;
    width: 258px;
    text-align: right;
    font-family: "Fira Sans", sans-serif;
  }
  .identity__name {
    font-weight: 600;
    font-size: 19px;
    letter-spacing: 0.2px;
    line-height: 1.2;
  }
  .identity__letters {
    font-size: 14px;
    color: var(--ink-soft);
    margin-top: 3px;
  }
  .divider {
    position: absolute;
    left: 556px;
    top: 52px;
    width: 2px;
    height: 176px;
  }
  .contact {
    position: absolute;
    left: 574px;
    top: 56px;
    font-family: "Crimson Pro", serif;
    font-size: 13px;
    line-height: 21px;
    color: var(--ink-soft);
    list-style: none;
  }
  .letter {
    position: absolute;
    left: 113px;
    top: 358px;
    width: 630px;
  }
  .letter__heading {
    font-family: "Fira Sans", sans-serif;
    font-weight: 600;
    font-size: 32px;
    letter-spacing: -0.3px;
    margin-bottom: 22px;
  }
  .letter__body p {
    font-family: "Crimson Pro", serif;
    font-size: 14.6px;
    line-height: 17.4px;
    text-align: justify;
    color: var(--ink);
    margin-bottom: 17px;
  }
</style>
</head>
<body>
  <main class="sheet">
    <header>
      <div class="identity">
        <div class="identity__name">Dr Lena Morwen Ostrow</div>
        <div class="identity__letters">MA PhD MRCP MRCPsych</div>
      </div>
      <svg class="divider" viewBox="0 0 2 176" aria-hidden="true">
        <line x1="1" y1="0" x2="1" y2="176" stroke="var(--rule)" stroke-width="1.4" stroke-dasharray="2 3"/>
      </svg>
      <ul class="contact">
        <li>BPR number 3819057</li>
        <li>17, Calloway Street</li>
        <li>London N4K 2TB</li>
        <li>t: 07812 430276</li>
        <li>e: lena.m.ostrow@dovrel.ac.uk</li>
      </ul>
    </header>

    <article class="letter">
      <h1 class="letter__heading">Sample text</h1>
      <div class="letter__body">
        <p>Facepersped inci aut entur alit que imillabora quiam doluptiosse simenti orepudion consed utae dolutatet quid est.</p>
        <p>Nullore rorenih illigenia nonet, acerendaepro conserum quae con eum corro excerit mos ratectatium que in plandita qui idia consereprem voluptia voluptatur audaepedi ipsam quunt escipsandem aut ea conectus aut modi denim faciae velecatem ipid minendam aborent aliqui dest, vero doluptat.</p>
        <p>Ga. Ut et, consequam intia de num fuga. Ut quam escilet lant es consecto explique volo et acerit quunt, si nobisci doluptatur?</p>
        <p>Mus alignimenis endunt qui aut esto excepororro ipsumus rem dolorem aut aut harum il num nis abo. Equod molor anda aut modit,Post, simodi doluptint exped molupta que natumquam dolutas rent que aute et ma comnihicilit prorququam volorio nonsequatem que etur? Quiscilique none pa dollaut estetur! Ignihite cores vendit doluptas nihillore nonsequist faccum fugitas reium et, saereium mus sit mosto te volest, ad ut ullitiorest eaquo non ipsunt, captatur aped ut odicitis sam expervo bla niet, conse veloris tatiorae libus il il moluptati tem faccus, que sus cum quis aut hictatur aceperitis abor arum alicipsunt eos mintius magnatem eum ut que porestior sae volesti oriorae. Perchil ignis id quae explamus vero ium spicat es eumet, sedi sinciamqui nonsequam quaspici ceritatur?</p>
        <p>Ga. Et quiscia sciendi ut duntus volecus et omnisinim aspita sunt omnimolori cor sequi offici beachit rem faceptio voluptat la seque cus sati occum id quate laudaepudit quiduntem et quiatque omnis quia veliqui Edis volest eossuntatiat inum quae liquide llendam, officia sita pratian daeccarum, quuntur molor sae core pre brernequa que doluptaque endit aut eos autem esquidi stistius nus nat landissum vit eum qui audist.</p>
      </div>
    </article>
  </main>
</body>
</html>
```